Redesign Fruit Juice Label Apple&Goji make it more valuable

Need to have redesigned my label (see attached WELVARDHOF_ETK_APFELGOJI..)- please use text from the old label (including the logo bergkrongoji - SEE updated text in MUST HAVES). The colours can vary.

The new label should be
- keep it minimalistic
- hipster

The target market are luxury segments, like 5 star hotels.
The bottle will remain the same (high 162,6mm, diameter 52,1mm) - the bottle size you find under the attached "BOTTLE SIZES". Here the link to the bottle:
http://www.plumavex.com/product_info.php/cPath/5_6/products_id/249
There will be a red tap and not a gold one (see attached RED TAP).

I attached some examples of labels I like (Example 1 - 4). The size of the label on the bottle can vary as you like, also possible if divided in two parts (no problem for the labelling machine). www.bergkron-goji.example

Reason: Because of the many designs the deadline has been extended the whole week. Please make your changes, so that I can make the final decision.

Target Market(s)

5 Star Hotels, health organic markets, wellness spa

Requirements
Must have
• Logo, text and barcode - attention the text is in three languages German - Italian - English please use a delimiter symbol (I used -) to separate them (or make it visible in an other way). Plese FELIX GRAF MERTEL has also to be marked (or make it visible)
• TEXT:
• Gojibeeren - Bacche di goji - Gojiberries (Lycium barbarum)
• Die wundersame Frucht aus dem Herzen Südtirols reich an Vitalstoffen.
• Il frutto miracoloso dal cuore delle Dolomiti, ricco di sostanze vitali.
• The miracle fruit from the heart of the Dolomites, high in vital nutrients.
• apfel - mela - apple
• Goji Lycium barbarum
• 100% saft - succo - juice
• Südtirol - Alto Adige
• www.bergkron-goji.example
• Zutaten - Ingredienti - Ingredients
• Apfelsaft naturtrüb (90 %) und Gojisaft – Lycium barbarum (10 %)
• succo di mela torbido (90 %) e succo di goji – Lycium barbarum (10 %)
• unfiltered apple juice (90 %) and goji juice – Lycium barbarum (10 %)
• Hergestellt für - Prodotto per
• Welvardhof Via Roseto 17 I-39088 Egna Felix Graf Mertel
• info@bergkron-goji.example
• Non disperdere nell’ambiente (HAS TO BE AT LEAST 2MM HIGH)
• Vor Gebrauch gut schütteln - Agitare bene prima dell’apertura - shake it before opening
• 200 ml (WITH THE E AND BARCODE)
• Nach dem Öffnen im Kühlschrank aufbewahren und innerhalb weniger
• Tage verbrauchen - Da conservare in frigorifero e consumare entro
• pochi giorni - After opening store in the refrigerator and consume
• within next few days
• Mindestens haltbar bis: Da consumarsi preferibilmente entro:
• Best before: 30.06.2018
Nice to have
• I like hand paintings
Should not have
• The Label should not look cheap

```html
<!DOCTYPE html>
<html lang="en">
<head>
<meta charset="utf-8">
<title>Bergkrongoji – Apple &amp; Goji Juice Labels</title>
<link rel="stylesheet" href="https://fonts.googleapis.com/css2?family=Josefin+Slab:wght@400;600;700&display=swap">
<style>
  :root {
    --canvas: #ffffff;
    --juice: #e9713a;
    --juice-deep: #e0632f;
    --seal: #ffffff;
    --brand-ink: #2b2b2b;
    --ink-gold: #f7b21b;
    --ink-wine: #9a1c26;
    --ink-white: #ffffff;
  }
  * { box-sizing: border-box; margin: 0; padding: 0; }
  html, body {
    width: 1200px; height: 1000px; overflow: hidden;
    background: var(--canvas);
    font-family: "Josefin Slab", Georgia, serif;
  }
  .canvas { position: relative; width: 1200px; height: 1000px; }

  .label {
    position: absolute; top: 470px;
    width: 176px; height: 330px;
    background: linear-gradient(180deg, var(--juice) 0%, var(--juice-deep) 100%);
    border-radius: 18px;
    display: flex; flex-direction: column; align-items: center;
    color: var(--ink);
  }
  .label--gold  { left: 82px;  --ink: var(--ink-gold); }
  .label--wine  { left: 332px; --ink: var(--ink-wine); }
  .label--white { left: 582px; --ink: var(--ink-white); }
  .label--compact { left: 942px; --ink: var(--ink-white); }

  .seal {
    margin-top: 20px;
    width: 98px; height: 98px; border-radius: 50%;
    background: var(--seal);
    display: flex; align-items: center; justify-content: center;
  }
  .seal__name {
    font-weight: 700; font-size: 14px; color: var(--brand-ink);
    letter-spacing: -0.2px;
  }

  .panel {
    margin-top: 10px; width: 100px;
    display: flex; flex-direction: column; align-items: center;
    text-align: center; line-height: 1;
  }
  .ornament {
    width: 64px; height: 12px; border-radius: 6px;
    background: var(--ink); opacity: 0.85;
  }
  .langs {
    font-size: 9.5px; font-weight: 600; margin-top: 4px;
    letter-spacing: 0.2px; white-space: nowrap;
  }
  .goji { font-size: 15px; font-weight: 600; margin-top: 1px; }
  .species { font-size: 9.5px; font-weight: 600; letter-spacing: 0.4px; }
  .rule { width: 96px; height: 1px; background: var(--ink); margin: 3px 0 4px; opacity: 0.8; }
  .percent { font-size: 27px; font-weight: 400; }
  .maker { font-size: 7.5px; font-weight: 700; margin-top: 6px; letter-spacing: 0.3px; white-space: nowrap; }
  .volume-row {
    margin-top: 8px; display: flex; align-items: center; gap: 4px;
    font-size: 7.5px; font-weight: 700;
  }
  .volume-row .dash { width: 24px; height: 1px; background: var(--ink); }
  .volume-row .dot { width: 5px; height: 5px; border-radius: 50%; background: var(--ink); }

  .label--compact .panel { width: 86px; margin-top: 12px; }
  .label--compact .langs, .label--compact .species { font-size: 8px; }
  .label--compact .goji { font-size: 13px; }
  .label--compact .percent { font-size: 23px; }
  .label--compact .rule { width: 80px; }
  .label--compact .ornament { width: 54px; height: 10px; }
</style>
</head>
<body>
<main class="canvas">

  <section class="label label--gold">
    <div class="seal"><span class="seal__name">bergkrongoji</span></div>
    <div class="panel">
      <div class="ornament" role="img" aria-label="Hand-drawn goji berry and leaf ornament"></div>
      <p class="langs">APFEL | MELA | APPLE</p>
      <p class="goji">&amp; GOJI</p>
      <p class="species">LYCIUM BARBARUM</p>
      <div class="rule"></div>
      <p class="percent">100%</p>
      <p class="langs">SAFT | SUCCO | JUICE</p>
      <p class="maker">FELIX GRAF MERTEL</p>
      <div class="volume-row"><span class="dot"></span><span class="dash"></span>200ML<span class="dash"></span><span class="dot"></span></div>
    </div>
  </section>

  <section class="label label--wine">
    <div class="seal"><span class="seal__name">bergkrongoji</span></div>
    <div class="panel">
      <div class="ornament" role="img" aria-label="Hand-drawn goji berry and leaf ornament"></div>
      <p class="langs">APFEL | MELA | APPLE</p>
      <p class="goji">&amp; GOJI</p>
      <p class="species">LYCIUM BARBARUM</p>
      <div class="rule"></div>
      <p class="percent">100%</p>
      <p class="langs">SAFT | SUCCO | JUICE</p>
      <p class="maker">FELIX GRAF MERTEL</p>
      <div class="volume-row"><span class="dot"></span><span class="dash"></span>200ML<span class="dash"></span><span class="dot"></span></div>
    </div>
  </section>

  <section class="label label--white">
    <div class="seal"><span class="seal__name">bergkrongoji</span></div>
    <div class="panel">
      <div class="ornament" role="img" aria-label="Hand-drawn goji berry and leaf ornament"></div>
      <p class="langs">APFEL | MELA | APPLE</p>
      <p class="goji">&amp; GOJI</p>
      <p class="species">LYCIUM BARBARUM</p>
      <div class="rule"></div>
      <p class="percent">100%</p>
      <p class="langs">SAFT | SUCCO | JUICE</p>
      <p class="maker">FELIX GRAF MERTEL</p>
      <div class="volume-row"><span class="dot"></span><span class="dash"></span>200ML<span class="dash"></span><span class="dot"></span></div>
    </div>
  </section>

  <section class="label label--compact">
    <div class="seal"><span class="seal__name">bergkrongoji</span></div>
    <div class="panel">
      <div class="ornament" role="img" aria-label="Hand-drawn goji berry and leaf ornament"></div>
      <p class="langs">APFEL | MELA | APPLE</p>
      <p class="goji">&amp; GOJI</p>
      <p class="species">LYCIUM BARBARUM</p>
      <div class="rule"></div>
      <p class="percent">100%</p>
      <p class="langs">SAFT | SUCCO | JUICE</p>
      <p class="maker">FELIX GRAF MERTEL</p>
      <div class="volume-row"><span class="dot"></span><span class="dash"></span>200ML<span class="dash"></span><span class="dot"></span></div>
    </div>
  </section>

</main>
</body>
</html>
```